Brightbuns Business Card Design

Our company is called Brightbuns. We manufacture confectionary snacks & frozen novelties. Our initial product portfolio includes frozen ice lollies/popsicles & stick ice cream bars.

We require a business card design.

Please use the attached Logo.

Please use an orange, brown, yellow colour code. You may choose any combination of the 3 or include all three. The logo however must remain orange.

Target Market(s)

Business card will be targeted at distributors of our products such as supermarket procurement managers, convenience store owners, wholesale distributors and merchandising agents.

Industry/Entity Type

Business

Requirements
Must have
• Kelvin Marsh_Director/ P.O.Box Westhollow 5172, Accra, Ghana / m: 00233(0)507318264/ e: kelvin.marsh@fernpost.co.uk

```html
<!DOCTYPE html>
<html lang="en">
<head>
<meta charset="utf-8">
<title>Brightbuns – Business Card</title>
<link href="https://fonts.googleapis.com/css2?family=Comic+Neue:wght@700&display=swap" rel="stylesheet">
<style>
  :root {
    --card-white: #ffffff;
    --maroon: #8a0f10;
    --brand-orange: #f25a14;
    --wordmark-faint: #f7cfc1;
  }
  html, body {
    margin: 0;
    padding: 0;
    overflow: hidden;
    background: var(--card-white);
  }
  .card {
    position: relative;
    width: 1200px;
    height: 693px;
    overflow: hidden;
    background: var(--card-white);
    font-family: "Comic Neue", "Comic Sans MS", cursive;
    font-weight: 700;
    font-style: normal;
    color: var(--maroon);
  }
  .backdrop-wordmark {
    position: absolute;
    left: 0;
    width: 1200px;
    top: 8px;
    margin: 0;
    text-align: center;
    font-size: 190px;
    line-height: 1;
    color: var(--wordmark-faint);
    white-space: nowrap;
  }
  .card-bands {
    position: absolute;
    inset: 0;
    width: 1200px;
    height: 693px;
  }
  .brand-name {
    position: absolute;
    left: 0;
    width: 1200px;
    top: 205px;
    margin: 0;
    text-align: center;
    font-size: 100px;
    font-weight: 700;
    line-height: 1;
    color: var(--brand-orange);
    white-space: nowrap;
  }
  .holder {
    position: absolute;
    left: 53px;
    top: 350px;
    margin: 0;
    font-style: normal;
    white-space: nowrap;
  }
  .holder-name {
    display: block;
    font-size: 52px;
    line-height: 60px;
  }
  .holder-address {
    display: block;
    font-size: 46px;
    line-height: 68px;
  }
  .contact {
    position: absolute;
    left: 615px;
    top: 470px;
    margin: 0;
    font-size: 40px;
    line-height: 52px;
    white-space: nowrap;
  }
</style>
</head>
<body>
  <main class="card">
    <p class="backdrop-wordmark" aria-hidden="true">Brightbuns</p>

    <svg class="card-bands" viewBox="0 0 1063 614" preserveAspectRatio="none" aria-hidden="true">
      <path class="top-band" d="M0,155 Q520,360 1063,195 L1063,225 Q520,385 0,190 Z" fill="var(--maroon)"/>
      <path class="bottom-band" d="M0,492 Q530,600 1063,515 L1063,614 L0,614 Z" fill="var(--maroon)"/>
    </svg>

    <h1 class="brand-name">Brightbuns</h1>

    <address class="holder">
      <span class="holder-name">Kelvin Marsh_Director</span>
      <span class="holder-address">P.O.Box Westhollow 5172</span>
      <span class="holder-address">Accra, Ghana</span>
    </address>

    <p class="contact">
      m: 00233(0)507318264<br>
      e: kelvin.marsh@fernpost.co.uk
    </p>
  </main>
</body>
</html>
```